Premium Wagyu Smallgoods Packaging Design (A5)

Hi there,
We are Silver Ridge Wagyu; a wagyu beef company based in Christchurch, New Zealand. We are needing new packaging for our new line of wagyu smallgoods (salami, braesola, fina seca etc.).
About us: Silver Ridge Wagyu began in 2015 and has since been tirelessly rearing stock to the quality and levels needed to supply the best restaurants and consumers. We combine the origin of Japanese breeding genetics and 200 year old techniques with New Zealand’s grass, grain, water and air.
Website:
https://silverridgemeats.example.nz/
Brand Guidelines:
https://brandpages.example.com/view/silverridgestyleguide/home?authuser=0
The smallgoods packaging designs should have consistent branding, with only the product names and colours changing across the designs. The placement of the gold foil needs to be consistent across all the designs.
The packaging dimensions are 17 x 24 cm.
The required components that need to be on the FRONT of the packaging are:
- Our logo
- The product weight
- The product name
The required components that need to be on the BACK of the packaging are:
- Proudly Farmed in New Zealand
- Keep chilled at or below 4°c
- 42 Tamsin Street, Fernhill, Christchurch, New Zealand
- Spaceholder text (we will include some information about the brand)
- Gold medals/badges to emphasize our main selling points
Attached are some drafts as well as our logos. If you need additional imagery or further questions please don't hesitate to contact us at the following emails below:
contact@silverridgemeats.example.nz
gemma@silverridgemeats.example.nz

```html
<!DOCTYPE html>
<html lang="en">
<head>
<meta charset="utf-8">
<title>Silver Ridge Wagyu – Smallgoods Packs</title>
<link rel="stylesheet" href="https://fonts.googleapis.com/css2?family=Jost:wght@400;600;700&display=swap">
<style>
  :root {
    --backdrop: #87a0ac;
    --pack-black: #000000;
    --accent-red: #e8363b;
    --foil-gold: #a58e70;
    --logo-white: #ffffff;
    --meat-light: #e59a95;
    --meat-mid: #c9575a;
    --meat-deep: #a33a3e;
  }
  * { margin: 0; padding: 0; box-sizing: border-box; }
  html, body { width: 1200px; height: 1200px; overflow: hidden; }
  body {
    background: var(--backdrop);
    position: relative;
    font-family: "Jost", sans-serif;
  }
  .pack {
    position: absolute;
    top: 237px;
    width: 515px;
    height: 727px;
    background: var(--pack-black);
    overflow: hidden;
  }
  .pack--fina-seca { left: 66px; }
  .pack--bresaola { left: 618px; }

  .pack__corner {
    position: absolute;
    left: 0; top: 0;
    width: 145px; height: 309px;
  }
  .pack__hanger {
    position: absolute;
    left: 218px; top: 35px;
    width: 78px; height: 42px;
  }
  .pack__seal {
    position: absolute;
    left: 382px; top: 36px;
    width: 96px; height: 96px;
  }
  .brand-name {
    position: absolute;
    left: 0; right: 0;
    top: 112px;
    text-align: center;
    color: var(--logo-white);
    font-weight: 700;
    font-size: 41px;
    line-height: 57px;
    letter-spacing: 0.42em;
    text-indent: 0.42em;
  }
  .product-window {
    position: absolute;
    left: 97px; top: 246px;
    width: 320px; height: 320px;
    border-radius: 50%;
    border: 9px solid var(--foil-gold);
  }
  .pack--fina-seca .product-window {
    background: radial-gradient(circle at 45% 40%, var(--meat-light) 0%, var(--meat-mid) 55%, var(--meat-deep) 100%);
  }
  .pack--bresaola .product-window {
    background: radial-gradient(circle at 55% 45%, #eaa29b 0%, #d9706e 55%, #3a2222 100%);
  }
  .name-band {
    position: absolute;
    left: 0; right: 0;
    top: 584px;
    height: 67px;
    border-top: 3px solid var(--foil-gold);
    border-bottom: 3px solid var(--foil-gold);
    display: flex;
    align-items: center;
    justify-content: center;
  }
  .product-name {
    color: var(--foil-gold);
    font-weight: 600;
    font-size: 34px;
    letter-spacing: 0.06em;
  }
  .net-weight {
    position: absolute;
    left: 0; right: 0;
    top: 672px;
    text-align: center;
    color: var(--foil-gold);
    font-weight: 400;
    font-size: 21px;
  }
</style>
</head>
<body>

<section class="pack pack--fina-seca">
  <svg class="pack__corner" viewBox="0 0 145 309"><polygon points="0,0 145,0 0,309" fill="var(--accent-red)"/></svg>
  <svg class="pack__hanger" viewBox="0 0 78 42"><path d="M12 18 H26 C28 18 28 0 39 0 C50 0 50 18 52 18 H66 A12 12 0 0 1 66 42 H12 A12 12 0 0 1 12 18 Z" fill="var(--backdrop)"/></svg>
  <svg class="pack__seal" viewBox="0 0 96 96" role="img" aria-label="Grain fed seal">
    <circle cx="48" cy="48" r="46" fill="none" stroke="var(--foil-gold)" stroke-width="2"/>
    <circle cx="48" cy="48" r="42" fill="none" stroke="var(--foil-gold)" stroke-width="1"/>
  </svg>
  <h1 class="brand-name">SILVER<br>RIDGE</h1>
  <div class="product-window" role="img" aria-label="Photograph of sliced wagyu fina seca with a white cattle silhouette"></div>
  <div class="name-band"><h2 class="product-name">WAGYU FINA SECA</h2></div>
  <p class="net-weight">80 g</p>
</section>

<section class="pack pack--bresaola">
  <svg class="pack__corner" viewBox="0 0 145 309"><polygon points="0,0 145,0 0,309" fill="var(--accent-red)"/></svg>
  <svg class="pack__hanger" viewBox="0 0 78 42"><path d="M12 18 H26 C28 18 28 0 39 0 C50 0 50 18 52 18 H66 A12 12 0 0 1 66 42 H12 A12 12 0 0 1 12 18 Z" fill="var(--backdrop)"/></svg>
  <svg class="pack__seal" viewBox="0 0 96 96" role="img" aria-label="Grain fed seal">
    <circle cx="48" cy="48" r="46" fill="none" stroke="var(--foil-gold)" stroke-width="2"/>
    <circle cx="48" cy="48" r="42" fill="none" stroke="var(--foil-gold)" stroke-width="1"/>
  </svg>
  <h1 class="brand-name">SILVER<br>RIDGE</h1>
  <div class="product-window" role="img" aria-label="Photograph of sliced wagyu bresaola with a white cattle silhouette"></div>
  <div class="name-band"><h2 class="product-name">WAGYU BRESAOLA</h2></div>
  <p class="net-weight">80 g</p>
</section>

</body>
</html>
```